Golden Coat All-Purpose Breading Bag Design

Our client, Harlow Food Products, is looking to re-design the packaging for their product, Pellworth's Golden Coat. Goldn Coat is an all-purpose food breading mix.

Harlow Foods has a registered trademark for this product, but they have not been using it for this particular 10 pound bag. They want to get the trademark onto the bag and also give the bag an updated look. They would like to continue to use the same red and blue colors. This 10 pound bag is not available on store shelves; it is sold to food service distributors who sell to restaurants.

All of the copy on the existing bag is still relevant, so we will want to incoprporate it into the bag design. Once these bags are filled with product, the tops get folded over about 1 inch and then sewn shut with thread.

Eventually, we will need the design applied to the Bag Template file attached, but that isn't important until a design is selected.

Target Market(s)

Restaurants

Industry/Entity Type

Food Manufacturing

Colors
0054AA
0677BA
7BADD7
CADEEF
E8F1F8
EB3D1F
EC4F4E
F09395
F8D3D4
FCEDEE

Requirements
Must have
• Trademark introduced to the design

```html
<!DOCTYPE html>
<html lang="en">
<head>
<meta charset="utf-8">
<title>Pellworth's Golden Coat – Bag Front</title>
<link rel="stylesheet" href="https://fonts.googleapis.com/css2?family=Kaushan+Script&family=Kalam:wght@700&family=Nunito:wght@800;900&display=block">
<style>
  :root {
    --navy: #213a82;
    --red: #cf2027;
    --tag-red: #c4202a;
    --white: #ffffff;
    --page: #ffffff;
    --wood-light: #f3e6d3;
    --wood: #d7b48a;
    --wood-dark: #b98a58;
    --food: #d68a3c;
  }
  * { margin: 0; padding: 0; box-sizing: border-box; }
  html, body { width: 1200px; height: 953px; overflow: hidden; background: var(--page); }
  .bag-front {
    position: absolute; left: 335px; top: 36px;
    width: 530px; height: 881px; overflow: hidden;
  }
  .shapes { position: absolute; inset: 0; width: 530px; height: 881px; }
  .product-photo {
    position: absolute; left: 0; top: 423px; width: 530px; height: 458px;
    background: linear-gradient(180deg, var(--white) 0%, var(--wood-light) 14%, var(--wood) 55%, var(--wood-dark) 100%);
  }
  .product-photo .food {
    position: absolute; left: 0; right: 0; top: 120px; height: 250px;
    background: radial-gradient(ellipse at 50% 50%, var(--food) 0%, #c9782e 55%, rgba(201,120,46,0) 80%);
  }
  .tagline {
    position: absolute; left: 95px; top: 14px; width: 350px;
    transform: rotate(-7deg); transform-origin: center;
    font-family: "Kalam", cursive; font-weight: 700; font-style: italic;
    color: var(--navy); text-transform: uppercase;
    font-size: 17px; line-height: 20px; text-align: center; letter-spacing: 0.3px;
  }
  .tagline .right-way {
    color: var(--tag-red);
    border-bottom: 2px solid var(--tag-red);
  }
  .script {
    position: absolute; font-family: "Kaushan Script", cursive;
    font-weight: 400; color: var(--white); line-height: 1; white-space: nowrap;
  }
  .brand-name { left: 119px; top: 96px; width: 292px; text-align: center; font-size: 42px; }
  .product-name.line-one { left: 72px; top: 178px; font-size: 96px; }
  .product-name.line-two { left: 240px; top: 268px; font-size: 92px; }
  .descriptor {
    position: absolute; left: 104px; top: 322px;
    font-family: "Nunito", sans-serif; font-weight: 900; color: var(--white);
    font-size: 19px; line-height: 20px; letter-spacing: 0.6px; text-align: center;
  }
  .claims {
    position: absolute; left: 109px; top: 428px; width: 315px; text-align: center;
    color: var(--white);
  }
  .claims .headline {
    font-family: "Nunito", sans-serif; font-weight: 900; font-size: 14.5px; letter-spacing: 1.4px;
  }
  .claims .detail {
    font-family: "Kalam", cursive; font-weight: 700; font-style: italic;
    font-size: 13px; line-height: 17px; text-transform: uppercase; margin-top: 3px;
  }
  .ingredients {
    position: absolute; left: 40px; top: 762px; width: 450px; text-align: center;
    font-family: "Nunito", sans-serif; font-weight: 900; font-size: 12.5px; line-height: 17px;
    color: var(--white); text-transform: uppercase;
    text-shadow: 0 0 3px var(--navy), 0 0 2px var(--navy), 1px 1px 0 var(--navy);
  }
  .net-weight {
    position: absolute; left: 0; top: 808px; width: 530px; text-align: center;
    font-family: "Nunito", sans-serif; font-weight: 900; font-size: 20px; letter-spacing: 0.8px;
    color: var(--white);
    text-shadow: 0 0 3px var(--navy), 0 0 2px var(--navy), 1px 1px 0 var(--navy);
  }
</style>
</head>
<body>
  <main class="bag-front">
    <div class="product-photo" role="img" aria-label="Photograph of golden fried chicken pieces on parchment paper on a wooden board">
      <div class="food"></div>
    </div>

    <svg class="shapes" viewBox="0 0 530 881" aria-hidden="true">
      <path class="top-banner" d="M119 83 Q265 48 411 73 L411 160 L119 160 Z" fill="var(--navy)"/>
      <path class="claims-panel" d="M109 397 L424 397 L424 540 L109 540 Z" fill="var(--navy)"/>
      <path class="name-banner" d="M36 195 Q240 142 504 158 L476 395 Q260 392 73 424 Z" fill="var(--red)"/>
    </svg>

    <p class="tagline">Chicken fried the Golden Coat way<br>is fried chicken <span class="right-way">the right way.</span></p>

    <p class="script brand-name">Pellworth's</p>
    <p class="script product-name line-one">Golden</p>
    <p class="script product-name line-two">Coat</p>
    <p class="descriptor">THE ALL<br>PURPOSE<br>BREADING</p>

    <div class="claims">
      <p class="headline">SEALS JUICE IN - GREASE OUT</p>
      <p class="detail">Cooks two-pound chicken well done<br>in 10 minutes (deep fat).</p>
    </div>

    <p class="ingredients">Ingredients: flour, salt, non-fat milk solids, egg yolk,<br>baking powder, corn starch, sugar and pepper.</p>
    <p class="net-weight">NET WT. 10 LBS.</p>
  </main>
</body>
</html>
```